Webpage design for a translation agancy

We need to update and modernize our current Wordpress webpage www.vindorelka.se. I am happy with the basics but there are definitely room for an update.
We are a translation agency providing translation services B2B. We supply translations to different industries. Law, HR, Medical, Financial, IT, Technical, Business. Our clients are mostly Swedish based companies.
We would like to see designs that:
- Increases our conversions
- Conveys reliance to our visitors/clients
- Keeps the framework on our current webpage (more or less)
- The quote bottom and quotation form is a crucial for our business. Drag and drop is a must.
-We'd like to keep the banner pics. One of them is our view from our office and the two others are local pictures from Stockholm/Sweden. The banner and the quote has to be integrated in the update.
-The design has to include designs for the whole webpage, landing page and all other pages.
/Tomas
Target Market(s)
Our target market is Swedish companies, b2b, operating in different industries. Law, Finance, Medical, IT, HR, Marketing, Engineering. Only B2B. Our typical buyer is a decision maker/ middle management.
Coding
Requirements
Must have
- - Conveys reliance to our visitors/clients
- - Our current Unique Selling Points
- - Keeps the framework on our current webpage (more or less)
- - The quote bottom and quotation form is a crucial for our business. One compeditor whom has a good solution for the quote form is, www.kelmarun.lv/en/
- -We'd like to keep the banner pics. One of them is our view from our office and the two others are local pictures from Stockholm/Sweden. The banner and the quote has to be integrated in the update.
- -The design has to include designs for the whole webpage, landing page and all other pages.
Nice to have
- Pretty much same color scales as today.

```html
<!DOCTYPE html>
<html lang="en">
<head>
<meta charset="utf-8">
<title>Vindorelka – Translation Agency</title>
<link href="https://fonts.googleapis.com/css2?family=Roboto:wght@300;400;500;700&family=Open+Sans:ital,wght@0,400;0,600;0,700;1,400&display=swap" rel="stylesheet">
<style>
:root{
  --green:#8dc63f;
  --yellow:#f2c15b;
  --teal:#2e5d6b;
  --purple:#9b5fd6;
  --blue:#5aaed8;
  --sky:#7cc4dc;
  --orange:#f39c3d;
  --red:#e0504a;
  --ink:#333;
  --muted:#777;
  --line:#e2e2e2;
  --grey-bg:#efefef;
  --accent:#8d6fc7;
}
*{box-sizing:border-box;margin:0;padding:0}
html,body{width:1200px;height:3689px;overflow:hidden}
body{font-family:"Open Sans",Arial,sans-serif;color:var(--ink);background:#fff;position:relative}
h1,h2,h3,h4{font-family:"Roboto",Arial,sans-serif;font-weight:400}
section,header,footer{position:relative;width:1200px}
.abs{position:absolute}
.rainbow{height:5px;background:linear-gradient(90deg,var(--blue) 0 20%,var(--green) 20% 40%,var(--yellow) 40% 60%,var(--orange) 60% 80%,var(--purple) 80% 100%)}

/* top bar + nav */
.topbar{height:30px;background:#fff;border-bottom:1px solid #f0f0f0}
.topbar ul{position:absolute;right:170px;top:9px;display:flex;gap:22px;list-style:none;font-size:11px;color:#555}
.topbar li::before{content:"";display:inline-block;width:7px;height:7px;border-radius:50%;background:var(--blue);margin-right:5px}
.nav{height:105px}
.logo{position:absolute;left:160px;top:62px;font-family:"Roboto",sans-serif;font-size:36px;font-weight:500;color:#555;letter-spacing:-.5px;line-height:1}
.nav ul{position:absolute;left:398px;top:80px;display:flex;gap:36px;list-style:none;font-size:13px;color:#444;font-family:"Roboto",sans-serif}

/* hero */
.hero{height:418px}
.hero-photo{position:absolute;inset:0;background:linear-gradient(180deg,#cfd4d8 0%,#eef0f2 45%,#d9dcdf 75%,#b9bec3 100%)}
.hero-band{position:absolute;left:0;top:155px;width:655px;height:103px;background:rgba(155,95,214,.88)}
.hero-band h1{position:absolute;left:178px;top:33px;color:#fff;font-size:30px;font-weight:500;letter-spacing:1px}
.arrow{position:absolute;top:190px;width:30px;height:30px}
.quote-btn{position:absolute;left:500px;top:389px;width:166px;height:49px;background:var(--green);color:#fff;font-family:"Roboto",sans-serif;font-size:16px;font-weight:500;text-align:center;line-height:49px;letter-spacing:.5px}

/* steps */
.steps{height:254px}
.step{position:absolute;top:43px;width:240px;text-align:left}
.step .circle{width:88px;height:88px;border-radius:50%;display:flex;align-items:center;justify-content:center}
.step p{margin-top:22px;font-family:"Roboto",sans-serif;font-size:16px;color:#333;white-space:nowrap}
.step-arrow{position:absolute;top:78px}
.cert{position:absolute;left:890px;top:55px;width:42px;height:52px;border:2px solid #3a7fc4;border-radius:3px;background:#eaf3fb}
.cert-note{position:absolute;left:890px;top:120px;display:flex;gap:8px;font-size:10px;color:#444;width:180px;line-height:1.35}
.cert-note span.dot{flex:none;width:20px;height:20px;border-radius:50%;border:2px solid #555}

/* about */
.about{height:415px;border-top:1px solid var(--line);overflow:hidden}
.about-shade{position:absolute;right:0;top:0;width:1200px;height:415px}
.about h2{position:absolute;left:160px;top:75px;font-size:30px;color:#222}
.about .copy{position:absolute;left:160px;top:135px;width:585px;font-size:11.5px;line-height:1.75;color:#444}
.about .copy p{margin-bottom:14px}
.map{position:absolute;left:728px;top:108px;width:340px;height:188px;border-radius:40% 45% 38% 50%;background:radial-gradient(ellipse at 40% 50%,#2d8fb8 0%,#3aa0c7 55%,rgba(58,160,199,0) 72%)}

/* why us */
.why{height:541px;border-top:1px solid var(--line)}
.why h2{position:absolute;left:160px;top:60px;font-size:30px;color:#222}
.why .intro{position:absolute;left:160px;top:123px;width:640px;font-size:11.5px;line-height:1.7;color:#444}
.feature{position:absolute;width:310px;display:flex;gap:20px}
.feature .ic{flex:none;width:80px;height:80px;border-radius:50%;background:#e9eef1;display:flex;align-items:center;justify-content:center}
.feature h4{font-size:14px;color:var(--blue);font-weight:500;margin:4px 0 8px;letter-spacing:.5px}
.feature p{font-size:11.5px;line-height:1.65;color:#555}
.why .divider{position:absolute;left:835px;top:60px;width:1px;height:420px;background:var(--line)}
.thumb{position:absolute;left:870px;top:45px;width:135px;height:140px;border-radius:50% 50% 20% 20%;background:linear-gradient(160deg,#4f8fd1,#2b62a8)}
.score{position:absolute;left:870px;top:200px;width:200px;text-align:center}
.score b{display:block;font-family:"Roboto",sans-serif;font-size:50px;color:var(--green);font-weight:500;line-height:1}
.score span{display:block;font-family:"Roboto",sans-serif;font-size:26px;color:#666;font-weight:300;line-height:1.25;margin-top:6px}
.score-quote{position:absolute;left:855px;top:345px;width:200px;font-size:11px;font-style:italic;line-height:1.6;color:#555}

/* industries */
.industries{height:585px;background:var(--grey-bg)}
.industries .notch{position:absolute;left:540px;top:-1px}
.industries h2{position:absolute;top:68px;width:100%;text-align:center;font-size:30px;color:#222}
.grid{position:absolute;left:160px;top:148px;width:880px;height:375px;display:grid;grid-template-columns:repeat(3,1fr);grid-template-rows:1fr 1fr}
.cell{text-align:center;padding-top:24px}
.cell:nth-child(-n+3){border-bottom:1px solid #d6d6d6}
.cell:not(:nth-child(3n)){border-right:1px solid #d6d6d6}
.cell h3{font-size:15px;font-weight:500;color:#222;margin:22px 0 10px}
.cell p{font-size:11.5px;color:#666;line-height:1.6;width:210px;margin:0 auto}
.cell svg{display:block;margin:0 auto}

/* testimonials */
.testimonials{height:349px;background:var(--sky)}
.testimonials h2{position:absolute;top:90px;width:100%;text-align:center;font-size:30px;color:#fff;font-weight:300}
.avatar{position:absolute;left:245px;top:158px;width:102px;height:102px;border-radius:50%;background:linear-gradient(160deg,#f6d9c4,#c96d52);border:4px solid #fff}
.testimonials blockquote{position:absolute;left:378px;top:163px;width:580px;font-size:12px;line-height:1.75;color:#fff;font-style:italic}
.testimonials cite{position:absolute;left:378px;top:240px;font-size:12px;font-style:normal;font-weight:600;color:#fff}
.dots{position:absolute;left:571px;top:290px;display:flex;gap:5px}
.dots i{width:11px;height:11px;border-radius:50%;background:rgba(255,255,255,.5)}
.dots i:first-child{background:#fff}

/* news */
.news{height:573px}
.news h2{position:absolute;top:50px;width:100%;text-align:center;font-size:30px;color:#222}
.news .intro{position:absolute;top:103px;left:340px;width:520px;text-align:center;font-size:11.5px;line-height:1.7;color:#444}
.card{position:absolute;top:175px;width:272px}
.card .photo{height:172px}
.card .social{display:flex;gap:12px;margin:14px 0 0 8px}
.card h3{font-size:16px;color:#222;margin:18px 0 12px}
.card p{font-size:11.5px;line-height:1.65;color:#444}
.card .meta{margin-top:14px;font-size:10px;color:var(--accent);display:flex;gap:12px}

/* clients */
.clients{height:111px;background:#f8f8f8;border-top:1px solid var(--line)}
.clients ul{position:absolute;left:160px;top:42px;width:880px;display:flex;justify-content:space-between;list-style:none;font-family:"Open Sans",sans-serif;font-size:15px;color:#777;font-weight:600}

/* footer */
.site-footer{height:308px;background:#f4f4f4}
.site-footer .logo{top:58px;font-size:34px}
.site-footer .about-text{position:absolute;left:160px;top:108px;width:215px;font-size:11.5px;line-height:1.7;color:#555}
.fcol{position:absolute;top:70px;font-size:11.5px;color:#555;line-height:1.6}
.fcol h4{font-family:"Roboto",sans-serif;font-size:13px;font-weight:700;color:#333;margin-bottom:14px}
.fcol li{list-style:none;margin-bottom:5px}
.fbottom{position:absolute;left:160px;right:160px;top:237px;border-top:1px solid #ddd}
.fsocial{position:absolute;left:160px;top:254px;display:flex;gap:6px}
.fsocial i{width:24px;height:24px;border-radius:50%;background:var(--sky)}
.legal{position:absolute;right:160px;top:260px;font-size:10.5px;color:#444;display:flex;gap:10px}
</style>
</head>
<body>

<div class="rainbow"></div>

<header>
  <div class="topbar">
    <ul><li>Contact us</li><li>Request a quote</li><li>Language ▾</li><li>Interpreter</li></ul>
  </div>
  <nav class="nav">
    <div class="logo">vindorelka</div>
    <ul><li>Our services</li><li>Translation methods</li><li>Customer cases</li><li>About us</li><li>Stockholm</li><li>For Translators</li></ul>
  </nav>
</header>

<section class="hero">
  <div class="hero-photo" role="img" aria-label="Office interior with a view through large windows over a Stockholm atrium"></div>
  <div class="hero-band"><h1>KVALITET AR VIKTIGT FOR OSS</h1></div>
  <svg class="arrow" style="left:52px" viewBox="0 0 30 30"><path d="M20 4 9 15l11 11" fill="none" stroke="#fff" stroke-width="2"/></svg>
  <svg class="arrow" style="left:1120px" viewBox="0 0 30 30"><path d="M10 4l11 11-11 11" fill="none" stroke="#fff" stroke-width="2"/></svg>
  <div class="quote-btn">REQUEST QUOTE</div>
</section>

<section class="steps">
  <div class="step" style="left:162px">
    <div class="circle" style="background:var(--green);margin-left:34px">
      <svg width="30" height="36" viewBox="0 0 30 36"><path d="M2 2h17l9 9v23H2z" fill="#fff"/><path d="M8 17h14M8 22h14M8 27h10" stroke="var(--green)" stroke-width="2"/></svg>
    </div>
    <p>1.REQUEST A QUOTE</p>
  </div>
  <svg class="step-arrow" style="left:355px" width="34" height="26" viewBox="0 0 34 26"><path d="M4 22c2-9 9-13 18-13V3l10 9-10 9v-6c-7 0-13 2-18 7z" fill="#888"/></svg>
  <div class="step" style="left:423px">
    <div class="circle" style="background:var(--yellow);margin-left:13px">
      <svg width="34" height="34" viewBox="0 0 34 34"><circle cx="14" cy="14" r="9" fill="none" stroke="#fff" stroke-width="4"/><path d="M21 21l9 9" stroke="#fff" stroke-width="5" stroke-linecap="round"/></svg>
    </div>
    <p>2.WE ANALYZE</p>
  </div>
  <svg class="step-arrow" style="left:580px" width="34" height="26" viewBox="0 0 34 26"><path d="M4 22c2-9 9-13 18-13V3l10 9-10 9v-6c-7 0-13 2-18 7z" fill="#888"/></svg>
  <div class="step" style="left:612px">
    <div class="circle" style="background:var(--teal);margin-left:62px">
      <svg width="36" height="26" viewBox="0 0 36 26"><rect x="1" y="1" width="34" height="24" rx="2" fill="#fff"/><path d="M2 3l16 12L34 3" fill="none" stroke="var(--teal)" stroke-width="2.5"/></svg>
    </div>
    <p>3.YOU'LL GET A FREE QUOTE</p>
  </div>
  <div class="cert"></div>
  <div class="cert-note"><span class="dot"></span><span>Endast professionella översättare</span></div>
</section>

<section class="about">
  <svg class="about-shade" viewBox="0 0 1200 415"><polygon points="762,0 1200,0 1200,415 725,415" fill="#f1f1f1"/></svg>
  <h2>Vindorelka Translation Agency</h2>
  <div class="copy">
    <p>Vindorelka is a translation agency that provides language services of the highest quality and maintains a strong focus on you, the customer. We assist our customers on a daily basis by translating industry-specific documentation to a wide variety of languages. Our project managers ensure that you receive expert help from our highly qualified specialist translators, who will adapt your text to the relevant target audience.</p>
    <p>Irrespective of whether your project comprises technical manuals, legal documentation, annual reports or websites, we can assist you. Our business concept is to provide translation services with a strong focus on personal service and quality.</p>
    <p>Our goal is always to build long-term partnerships with our customers.</p>
  </div>
  <div class="map" role="img" aria-label="Illustrated world map with colourful speech bubbles in many languages"></div>
</section>

<section class="why">
  <h2>Why Us?</h2>
  <p class="intro">Sed ut perspiciatis unde omnis iste natus error sit voluptatem accusantium doloremque laudantium, totam rem aperiam, eaque ipsa quae ab illo inventore veritatis et quasi architecto beata.</p>

  <div class="feature" style="left:160px;top:215px">
    <div class="ic"><svg width="38" height="42" viewBox="0 0 38 42"><circle cx="19" cy="15" r="12" fill="#7bb4cf"/><path d="M11 25l-5 15 8-4 5 5 0-14M27 25l5 15-8-4-5 5" fill="#7bb4cf"/></svg></div>
    <div><h4>QUALITY</h4><p>Vi fokuserar på att hålla hög kvalitet i alla delar av översättningsprocessen, från projektledning, översättning...</p></div>
  </div>
  <div class="feature" style="left:500px;top:215px">
    <div class="ic"><svg width="36" height="36" viewBox="0 0 36 36"><path d="M8 2l7 8-4 4c2 5 6 9 11 11l4-4 8 7-5 6C16 33 3 20 2 7z" fill="#7bb4cf"/></svg></div>
    <div><h4>DELIVERY</h4><p>Vi har som mål att inom samtliga våra uppdrag hålla bästa möjliga leveranstid och att leverera i format som</p></div>
  </div>
  <div class="feature" style="left:160px;top:365px">
    <div class="ic"><svg width="36" height="38" viewBox="0 0 36 38"><path d="M18 2c9 0 15 6 15 14 0 5-3 8-5 10v10H12v-6H6v-8H2l4-8C6 7 11 2 18 2z" fill="#7bb4cf"/></svg></div>
    <div><h4>COMPETENCE</h4><p>Som översättningsbyrå har vi krav på oss att alltid ligga steget före. Vi jobbar enbart med branschens mest.</p></div>
  </div>
  <div class="feature" style="left:500px;top:365px">
    <div class="ic"><svg width="38" height="38" viewBox="0 0 38 38"><circle cx="12" cy="12" r="9" fill="#7bb4cf"/><circle cx="12" cy="12" r="3" fill="#e9eef1"/><path d="M17 17l18 18M27 27l-4 4M32 32l-4 4" stroke="#7bb4cf" stroke-width="4"/></svg></div>
    <div><h4>SECRECY</h4><p>Vi behandlar alla våra kunders uppdrag och dokument med högsta krav på säkerhet och sekretess.</p></div>
  </div>

  <div class="divider"></div>
  <div class="thumb" role="img" aria-label="Illustrated thumbs-up hand"></div>
  <div class="score"><b>98%</b><span>Customer Satisfaction.</span></div>
  <p class="score-quote">Sed ut persp iciatisfore unde omlomis iste natu sit vol tat em ac cus an tiu moloiome laudo mtum otam remeriam, eaumus loqueru uar chitecto beata.</p>
</section>

<section class="industries">
  <svg class="notch" width="120" height="28" viewBox="0 0 120 28"><path d="M0 0h120c-30 0-40 28-60 28S30 0 0 0z" fill="#fff"/></svg>
  <h2>We know your industry</h2>
  <div class="grid">
    <div class="cell">
      <svg width="60" height="50" viewBox="0 0 60 50"><circle cx="22" cy="28" r="15" fill="none" stroke="var(--accent)" stroke-width="8" stroke-dasharray="6 4"/><circle cx="22" cy="28" r="6" fill="var(--accent)"/><circle cx="46" cy="12" r="9" fill="none" stroke="var(--accent)" stroke-width="6" stroke-dasharray="4 3"/></svg>
      <h3>Machine and Manufacturing</h3><p>We focus on high quality in all aspects of the translation process, from project</p>
    </div>
    <div class="cell">
      <svg width="56" height="50" viewBox="0 0 56 50"><rect x="14" y="4" width="26" height="14" rx="2" transform="rotate(-35 27 11)" fill="#d1a13c"/><path d="M28 18l18 24" stroke="#d1a13c" stroke-width="6" stroke-linecap="round"/><rect x="4" y="42" width="26" height="6" fill="#d1a13c"/></svg>
      <h3>Legal Translation</h3><p>We focus on high quality in all aspects of the translation process, from project</p>
    </div>
    <div class="cell">
      <svg width="50" height="50" viewBox="0 0 50 50"><circle cx="25" cy="25" r="21" fill="var(--green)"/><path d="M14 15c6-2 9 2 13 0 3 4-2 8 2 12-4 3-8 1-9 8-4-3-2-7-6-9 2-4-2-6 0-11z" fill="#fff"/></svg>
      <h3>IT/Webb</h3><p>We focus on high quality in all aspects of the translation process, from project</p>
    </div>
    <div class="cell">
      <svg width="60" height="44" viewBox="0 0 60 44"><rect x="4" y="8" width="52" height="30" fill="none" stroke="var(--blue)" stroke-width="4"/><circle cx="30" cy="23" r="7" fill="var(--blue)"/><path d="M10 14h6M44 32h6" stroke="var(--blue)" stroke-width="3"/></svg>
      <h3>Financial Translation</h3><p>We focus on high quality in all aspects of the translation process, from project</p>
    </div>
    <div class="cell">
      <svg width="56" height="44" viewBox="0 0 56 44"><path d="M4 40l12-22 10 12 10-24 14 34z" fill="#3b7fb5"/><path d="M2 42h52" stroke="#3b7fb5" stroke-width="3"/></svg>
      <h3>Marketing</h3><p>We focus on high quality in all aspects of the translation process, from project</p>
    </div>
    <div class="cell">
      <svg width="56" height="46" viewBox="0 0 56 46"><rect x="20" y="2" width="16" height="10" rx="2" fill="none" stroke="#e08a4a" stroke-width="4"/><rect x="4" y="10" width="48" height="34" rx="4" fill="#e08a4a"/><path d="M28 18v18M19 27h18" stroke="#fff" stroke-width="5"/></svg>
      <h3>Medical Translation</h3><p>We focus on high quality in all aspects of the translation process, from project</p>
    </div>
  </div>
</section>

<section class="testimonials">
  <h2>Our Testimonials</h2>
  <div class="avatar" role="img" aria-label="Illustrated customer portrait"></div>
  <blockquote>“ Sed ut perspiciatis unde omnis iste natus error sit voluptatem accusantium doloremque laudantium, totam rem aperiam, eaque ipsa quae ab illo inventore veritatis et quasi architecto beatae vitae dicta sunt explicabo. Nemo enim ipsam voluptatem quia voluptas sit aspernatur. ”</blockquote>
  <cite>Head of Fulfillment, City Name</cite>
  <div class="dots"><i></i><i></i><i></i><i></i></div>
</section>

<section class="news">
  <h2>Latest News</h2>
  <p class="intro">Sed ut perspiciatis unde omnis iste natus error sit voluptatem accusantium doloremque laudantium, totam rem aperiam, eaque ipsa quae ab illo inventore veritatis et quasi architecto beata.</p>

  <article class="card" style="left:160px">
    <div class="photo" role="img" aria-label="Photo of hands working at a laptop on a desk" style="background:linear-gradient(135deg,#c9b8a6,#8a7e74 60%,#d9d2c8)"></div>
    <div class="social"><svg width="60" height="12"><circle cx="5" cy="6" r="4" fill="#3b5f9e"/><circle cx="25" cy="6" r="4" fill="#4aa8e0"/><circle cx="45" cy="6" r="4" fill="#2a77b5"/></svg></div>
    <h3>Framtiden för världens språk</h3>
    <p>At vloreero eos et accusamus et accusamus ettodio noonimuspiditate non provident, similique sulonito ffi cia deserunt mollitia animi.</p>
    <div class="meta"><span>▣ 20 FEB 2017</span><span>|</span><span>◌ Comments (00)</span></div>
  </article>
  <article class="card" style="left:463px">
    <div class="photo" role="img" aria-label="Photo of a young plant growing from a jar of coins" style="background:linear-gradient(135deg,#f3e3b0,#b89a5a 55%,#6f8a3a)"></div>
    <div class="social"><svg width="60" height="12"><circle cx="5" cy="6" r="4" fill="#3b5f9e"/><circle cx="25" cy="6" r="4" fill="#4aa8e0"/><circle cx="45" cy="6" r="4" fill="#2a77b5"/></svg></div>
    <h3>Framtiden för världens språk</h3>
    <p>At vloreero eos et accusamus et accusamus ettodio noonimuspiditate non provident, similique sulonito ffi cia deserunt mollitia animi.</p>
    <div class="meta"><span>▣ 20 FEB 2017</span><span>|</span><span>◌ Comments (00)</span></div>
  </article>
  <article class="card" style="left:765px">
    <div class="photo" role="img" aria-label="Photo of business people shaking hands in an office" style="background:linear-gradient(135deg,#dfe6ee,#8ea3b8 55%,#3c4a5a)"></div>
    <div class="social"><svg width="60" height="12"><circle cx="5" cy="6" r="4" fill="#3b5f9e"/><circle cx="25" cy="6" r="4" fill="#4aa8e0"/><circle cx="45" cy="6" r="4" fill="#2a77b5"/></svg></div>
    <h3>Framtiden för världens språk</h3>
    <p>At vloreero eos et accusamus et accusamus ettodio noonimuspiditate non provident, similique sulonito ffi cia deserunt mollitia animi.</p>
    <div class="meta"><span>▣ 20 FEB 2017</span><span>|</span><span>◌ Comments (00)</span></div>
  </article>
</section>

<section class="clients">
  <ul><li>Fennmark</li><li>Ostlund &amp; Berg</li><li>Halvard Capital</li><li>Norvik Media</li><li>Solvik Travel</li><li>Kastrel</li></ul>
</section>

<footer class="site-footer">
  <div class="rainbow"></div>
  <div class="logo">vindorelka</div>
  <p class="about-text">Vindorelka is a translation agency that provides language services of the highest quality and maintains a strong focus on you, the customer.</p>
  <div class="fcol" style="left:408px"><h4>VINDORELKA AB</h4><ul><li>Request a Quote</li><li>Contact</li><li>About Vindorelka</li><li>VAT: SE000000000001</li></ul></div>
  <div class="fcol" style="left:588px"><h4>TRANSLATION SERVICES</h4><ul><li>Technical translations</li><li>Legal Translations</li><li>Financial translations</li><li>Medical translations</li></ul></div>
  <div class="fcol" style="left:790px"><h4>ABOUT US</h4><ul><li>News</li><li>About us</li><li>Contact us</li></ul></div>
  <div class="fcol" style="left:925px"><h4>VINDORELKA AB</h4><ul><li>Ekvägen 12,</li><li>111 22, Stockholm</li><li>+46 8 000 12 34</li></ul></div>
  <div class="fbottom"></div>
  <div class="fsocial"><i></i><i></i><i></i><i></i></div>
  <div class="legal"><span>© 2017 Vindorelka. All Copyrights are Reserved.Terms of Use</span><span>Privacy Policy</span><span>Sitemap</span></div>
</footer>

</body>
</html>
```